Brenvick Holdings LLC, new Business cards

I'm moving offices and need new cards. Plus I'm open to modifying the current design of my card. I will keep the logo but would like to explore other layouts and fonts for the design. I've included the current double sided card for reference. I Like the navy color and white. Might be open to grays or silver. Needs to be clean and elegant.

Target Market(s)

Investors, buyers & sellers of private equities and real estate.

Contact Information for Business Card

Brenvick Holdings
Dorian P.K. Halvers, Managing Principal
418 Ostrander Ave., Suite 612
Denver, CO 80319
M: 970-555-0147, O: 303-555-0192
Dorian@brenvickholdings.example
Brenvickholdings.example

Colors
0354a2
ffffff
c4c4c4

Requirements
Must have
• Business card details.
• Logo raised or embossed, it was designed after a wax seal. Current has raised ink.
Nice to have
• Space on card to write additional notes.

```html
<!DOCTYPE html>
<html lang="en">
<head>
<meta charset="utf-8">
<title>Brenvick Holdings – Business Card</title>
<link rel="stylesheet" href="https://fonts.googleapis.com/css2?family=Source+Sans+3:wght@400;600&display=swap">
<style>
  :root {
    --backdrop: #e6e6e8;
    --card: #ffffff;
    --navy: #2a2858;
    --ink: #1c1c24;
    --accent: #5a55a8;
    --icon: #3a3772;
  }
  * { margin: 0; padding: 0; box-sizing: border-box; }
  html, body {
    width: 1200px; height: 1024px; overflow: hidden;
    background: var(--backdrop);
    font-family: "Source Sans 3", "Myriad Pro", Arial, sans-serif;
  }
  .card {
    position: absolute; left: 75px; top: 212px;
    width: 1050px; height: 600px;
    background: var(--card);
    border-radius: 36px;
    box-shadow: 0 6px 24px rgba(0,0,0,.12);
  }
  .brand {
    position: absolute; right: 150px; top: 70px;
    display: flex; align-items: center; gap: 18px;
  }
  .brand-dot {
    width: 64px; height: 64px; border-radius: 50%;
    background: var(--navy);
  }
  .brand-name {
    font-size: 34px; font-weight: 600; color: var(--navy);
    letter-spacing: 0.5px;
  }
  .identity {
    position: absolute; left: 110px; top: 222px;
  }
  .person-name {
    font-size: 46px; font-weight: 400; color: var(--ink); line-height: 1.05;
  }
  .person-title {
    font-size: 30px; color: var(--accent); line-height: 1.2;
  }
  .divider {
    position: absolute; left: 110px; right: 100px; top: 332px;
    height: 4px; background: var(--navy);
  }
  .contact-list {
    position: absolute; left: 110px; top: 368px;
    list-style: none;
  }
  .contact-list li, .location-list li {
    display: flex; align-items: center; gap: 16px;
    font-size: 27px; color: var(--ink); height: 40px;
  }
  .location-list {
    position: absolute; right: 100px; top: 92px;
    list-style: none; text-align: right;
  }
  .location-list li { justify-content: flex-end; }
  .location-list .no-icon { padding-right: 42px; }
  .icon {
    width: 26px; height: 26px; flex: none;
  }
  .location-list { top: 368px; }
</style>
</head>
<body>
  <div class="card">
    <div class="brand">
      <span class="brand-dot"></span>
      <span class="brand-name">Brenvick Holdings</span>
    </div>

    <div class="identity">
      <div class="person-name">Dorian P.K. Halvers</div>
      <div class="person-title">Managing Principal</div>
    </div>

    <div class="divider"></div>

    <ul class="contact-list">
      <li>
        <svg class="icon" viewBox="0 0 26 26"><rect width="26" height="26" rx="3" fill="var(--icon)"/><rect x="9" y="5" width="8" height="16" rx="1.5" fill="none" stroke="#fff" stroke-width="1.8"/></svg>
        970-555-0147
      </li>
      <li>
        <svg class="icon" viewBox="0 0 26 26"><rect width="26" height="26" rx="3" fill="var(--icon)"/><path d="M8 6c-2 2-1 7 4 12s9 5 11 3l-3-3-2 1c-2-1-4-3-5-5l1-2-3-3z" fill="#fff"/></svg>
        TBD
      </li>
      <li>
        <svg class="icon" viewBox="0 0 26 26"><rect width="26" height="26" rx="3" fill="var(--icon)"/><rect x="5" y="8" width="16" height="11" fill="none" stroke="#fff" stroke-width="1.8"/><path d="M5 8l8 6 8-6" fill="none" stroke="#fff" stroke-width="1.8"/></svg>
        Dorian@brenvickholdings.example
      </li>
    </ul>

    <ul class="location-list">
      <li>
        Brenvickholdings.example
        <svg class="icon" viewBox="0 0 26 26"><rect width="26" height="26" rx="3" fill="var(--icon)"/><circle cx="13" cy="13" r="7" fill="none" stroke="#fff" stroke-width="1.8"/><path d="M6 13h14M13 6c-3 4-3 10 0 14M13 6c3 4 3 10 0 14" fill="none" stroke="#fff" stroke-width="1.4"/></svg>
      </li>
      <li>
        418 Ostrander Ave., Suite 612
        <svg class="icon" viewBox="0 0 26 26"><rect width="26" height="26" rx="3" fill="var(--icon)"/><path d="M13 21s-6-6-6-10a6 6 0 0 1 12 0c0 4-6 10-6 10z" fill="#fff"/><circle cx="13" cy="11" r="2.2" fill="var(--icon)"/></svg>
      </li>
      <li class="no-icon">Denver, CO 80319</li>
    </ul>
  </div>
</body>
</html>
```